A private security company called "Tavrin Security Services Ltd"

Hello everybody,

We need a web page for a company based in NZ. It is mainly an informative website so it would be wonderful if the designer puts their absolute best into making it a website that I would really appreciate. The website needs to show professionalism and also needs to make our web surfers find the information they need in a click. the company's colour is black and silver, and if those two colours could be integrated into the website it would be absolutely lovely. Please do contact me for any information.

Sincerely,
Dorian Velasko

Industry/Entity Type

Security

```html
<!DOCTYPE html>
<html lang="en">
<head>
<meta charset="utf-8">
<title>Tavrin Security Services Ltd</title>
<link href="https://fonts.googleapis.com/css2?family=Alegreya:wght@700&family=Open+Sans:wght@400;600&display=swap" rel="stylesheet">
<style>
  :root {
    --bg-dark: #0d0c0a;
    --panel: #030303;
    --rule: #3d3d3d;
    --text: #ffffff;
    --muted: #c9c9c9;
    --accent: #e0141b;
  }
  * { margin: 0; padding: 0; box-sizing: border-box; }
  html, body { width: 1200px; height: 971px; overflow: hidden; }
  body {
    position: relative;
    font-family: "Open Sans", Arial, sans-serif;
    color: var(--text);
    background:
      radial-gradient(ellipse 180px 420px at 60px 520px, rgba(150,100,25,.55), transparent 70%),
      radial-gradient(ellipse 200px 420px at 1150px 420px, rgba(150,100,25,.5), transparent 70%),
      radial-gradient(ellipse 260px 120px at 430px 40px, rgba(130,90,25,.35), transparent 70%),
      radial-gradient(ellipse 500px 300px at 600px 500px, #1a1815, var(--bg-dark));
  }
  .brand {
    position: absolute; left: 110px; top: 60px;
    display: flex; align-items: center; gap: 10px;
    font-family: "Alegreya", Georgia, serif; font-weight: 700; font-size: 20px; color: var(--text);
    line-height: 1.1;
  }
  .brand-mark { width: 14px; height: 14px; background: var(--text); }
  .call {
    position: absolute; left: 860px; top: 52px; width: 220px; height: 54px;
    background: #050505; border-radius: 8px;
    font-size: 24px; color: var(--muted); text-align: center; line-height: 54px;
  }
  .main {
    position: absolute; left: 100px; top: 150px; width: 1000px; height: 737px;
    background: var(--panel);
  }
  .nav {
    position: absolute; left: 138px; top: 188px; width: 932px; height: 42px;
    background: linear-gradient(#252525, #161616);
  }
  .nav a {
    position: absolute; top: 10px;
    font-family: "Alegreya", Georgia, serif; font-weight: 700; font-size: 16px;
    color: var(--text); text-decoration: none;
  }
  .nav a.active, .footer-nav a.active { color: var(--accent); }
  .hero {
    position: absolute; left: 136px; top: 258px; width: 650px; height: 320px;
    background: linear-gradient(160deg, #6e5a3c 0%, #a88a5c 40%, #3a2e22 75%, #1b1815 100%);
  }
  .side-box {
    position: absolute; left: 820px; width: 248px;
    background: linear-gradient(#2a2a2a, #1e1e1e);
  }
  .side-box h2 {
    margin-top: 18px; height: 34px; width: 230px; padding-left: 15px;
    background: linear-gradient(90deg, #111 0%, #1a1a1a 60%, #3a3a3a 100%);
    font-family: "Alegreya", Georgia, serif; font-weight: 700; font-size: 19px; line-height: 32px;
  }
  .services { top: 258px; height: 295px; }
  .services ul { list-style: none; margin: 7px 17px 0 20px; }
  .services li {
    height: 40px; line-height: 40px; font-size: 13px;
    border-bottom: 1px solid var(--rule); padding-left: 15px; position: relative;
    white-space: nowrap;
  }
  .services li::before {
    content: ""; position: absolute; left: 0; top: 15px;
    border-left: 7px solid var(--accent);
    border-top: 5px solid transparent; border-bottom: 5px solid transparent;
  }
  .welcome { top: 607px; height: 235px; overflow: hidden; }
  .welcome h2 { margin-top: 14px; }
  .welcome p {
    margin: 10px 8px 0 15px; font-size: 12.5px; line-height: 21px;
    white-space: nowrap; letter-spacing: -0.1px;
  }
  .tile { position: absolute; top: 607px; width: 216px; height: 234px; }
  .tile-photo { position: absolute; inset: 0; }
  .tile-caption {
    position: absolute; left: 0; top: 81px; width: 100%; height: 93px;
    background: rgba(20,20,20,.88);
    font-family: "Alegreya", Georgia, serif; font-weight: 700; font-size: 18px;
    text-align: center; line-height: 84px; white-space: nowrap;
  }
  .footer {
    position: absolute; left: 110px; top: 886px; width: 980px; height: 46px;
    background: #0e0e0e;
  }
  .copyright { position: absolute; left: 28px; top: 17px; font-size: 12px; }
  .footer-nav { position: absolute; right: 20px; top: 18px; font-size: 13px; color: var(--text); white-space: nowrap; }
  .footer-nav a { color: var(--text); text-decoration: none; }
  .footer-nav span { margin: 0 5px; }
</style>
</head>
<body>
  <header>
    <div class="brand"><span class="brand-mark"></span><span>Tavrin<br>Security Services Ltd</span></div>
    <div class="call">Call: 123 456 7890</div>
  </header>

  <div class="main"></div>

  <nav class="nav">
    <a class="active" href="#" style="left:20px">Home</a>
    <a href="#" style="left:117px">About Us</a>
    <a href="#" style="left:242px">Security Services</a>
    <a href="#" style="left:421px">Why Us</a>
    <a href="#" style="left:533px">Testimonials</a>
    <a href="#" style="left:683px">Contct Us</a>
  </nav>

  <div class="hero" role="img" aria-label="Armed security officers helping a traveller in a busy station hall"></div>

  <aside class="side-box services">
    <h2>Security Services</h2>
    <ul>
      <li>Lorem ipsum dolor sit amet</li>
      <li>Consectetur adipisicing elit sed</li>
      <li>Do eiusmod tempor incididunt</li>
      <li>Ut labore et dolore magna</li>
      <li>AliquaUt enim ad minim</li>
    </ul>
  </aside>

  <section class="tile" style="left:138px">
    <div class="tile-photo" role="img" aria-label="Patrol officer with a guard dog beside a patrol car" style="background:linear-gradient(#7d8a7a,#3b3d3a 55%,#9a968e)"></div>
    <div class="tile-caption">Security Patrols</div>
  </section>
  <section class="tile" style="left:365px">
    <div class="tile-photo" role="img" aria-label="Uniformed security guard on duty" style="background:linear-gradient(#8fb0d4,#5a6b88 55%,#b8b4ae)"></div>
    <div class="tile-caption">Guard Services</div>
  </section>
  <section class="tile" style="left:592px">
    <div class="tile-photo" role="img" aria-label="Surveillance camera above a city skyline" style="background:linear-gradient(#5c9fe0,#a9c6e2 55%,#7a8a98)"></div>
    <div class="tile-caption">Fixed Camra Systems</div>
  </section>

  <aside class="side-box welcome">
    <h2>Welcome</h2>
    <p>Lorem ipsum dolor sit amet consecte-<br>tur adipisicing elit sed do eiusmod<br>tempor incididunt ut labore et dolore<br>magna aliqua ut enim ad minim<br>veniam, quis nostrud exercitation<br>ullamco laboris nisi ut aliquip ex ea<br>commodo consequat duis aute irure<br>dolor in reprehenderit in voluptate.</p>
  </aside>

  <footer class="footer">
    <div class="copyright">Copy rigthe 2014 ©Tavrin. All rights reserved</div>
    <div class="footer-nav">
      <a class="active" href="#">Home</a><span>|</span><a href="#">About Us</a><span>|</span><a href="#">Security Services</a><span>|</span><a href="#">Why Us</a><span>|</span><a href="#">Testimonials</a><span>|</span><a href="#">Contct Us</a>
    </div>
  </footer>
</body>
</html>
```